2019 Theater Season Posters

Seeking a 5-show 2019 theater season design. Each show should have its own look/feel but they should also coordinate together either by color or overall tone. Please review the PDF document for specific text needed and reference/inspiration imagery. In addition, I've attached the 2018 designs for reference on the concept.

Target Market(s)

new jersey theater goers

Font styles to use
Sans Serif

Colors

Designer to choose colors to be used in the design.

Requirements
Must have
• 5 distinct posters that coordinate together via color and tone
Nice to have
• simple, bold graphics that are memorable
Should not have
• Any existing logos or posers for these shows that could be found online.

```html
<!DOCTYPE html>
<html lang="en">
<head>
<meta charset="utf-8">
<title>12 Heated Voices — May 3-5</title>
<link rel="stylesheet" href="https://fonts.googleapis.com/css2?family=Montserrat:wght@500;700&display=swap">
<style>
  :root {
    --backdrop: #f3f2f0;
    --poster-bg: #403a2e;
    --poster-bg-deep: #3d372b;
    --gold: #e6a426;
    --lone-voice: #f7f7f5;
  }
  html, body {
    margin: 0;
    width: 1200px;
    height: 801px;
    overflow: hidden;
    background: var(--backdrop);
  }
  .poster {
    position: absolute;
    left: 322px;
    top: 0;
    width: 556px;
    height: 801px;
    background: linear-gradient(180deg, var(--poster-bg) 0%, var(--poster-bg-deep) 100%);
    font-family: "Montserrat", sans-serif;
    color: var(--gold);
  }
  .figure-grid {
    position: absolute;
    left: 0;
    top: 0;
    width: 556px;
    height: 430px;
  }
  .title-count {
    position: absolute;
    left: 0;
    width: 100%;
    top: 488px;
    margin: 0;
    text-align: center;
    font-weight: 700;
    font-size: 117px;
    line-height: 140px;
    letter-spacing: -2px;
  }
  .title-name {
    position: absolute;
    left: 0;
    width: 100%;
    top: 622px;
    margin: 0;
    text-align: center;
    font-weight: 700;
    font-size: 44px;
    line-height: 56px;
    letter-spacing: 0.5px;
    white-space: nowrap;
  }
  .run-dates {
    position: absolute;
    left: 0;
    width: 100%;
    top: 698px;
    margin: 0;
    text-align: center;
    font-weight: 500;
    font-size: 31px;
    line-height: 40px;
  }
</style>
</head>
<body>
  <main class="poster">
    <svg class="figure-grid" viewBox="0 0 556 430" xmlns="http://www.w3.org/2000/svg">
      <g fill="var(--gold)">
        <circle cx="100" cy="127" r="41" role="img" aria-label="Figure 1: shirt with plain necktie"/>
        <circle cx="219" cy="127" r="41" role="img" aria-label="Figure 2: blouse with round collar and buttons"/>
        <circle cx="338" cy="127" r="41" role="img" aria-label="Figure 3: shirt with striped necktie"/>
        <circle cx="456" cy="127" r="41" role="img" aria-label="Figure 4: shirt with slim necktie"/>
        <circle cx="100" cy="250" r="41" role="img" aria-label="Figure 5: collar with wide bow tie"/>
        <circle cx="219" cy="250" r="41" role="img" aria-label="Figure 6: shirt with collar and necktie"/>
        <circle cx="338" cy="250" r="41" role="img" aria-label="Figure 7: cap-sleeve blouse"/>
        <circle cx="456" cy="250" r="41" role="img" aria-label="Figure 8: sleeveless top"/>
        <circle cx="100" cy="373" r="41" role="img" aria-label="Figure 9: short-sleeve blouse"/>
        <circle cx="219" cy="373" r="41" role="img" aria-label="Figure 10: small bow tie"/>
        <circle cx="338" cy="373" r="41" role="img" aria-label="Figure 11: jacket lapels with necktie"/>
      </g>
      <circle cx="456" cy="373" r="41" fill="var(--lone-voice)" role="img" aria-label="Figure 12: white shirt with striped necktie, the lone dissenter"/>
    </svg>

    <h1 class="title-count">12</h1>
    <h2 class="title-name">HEATED VOICES</h2>
    <p class="run-dates">May 3-5</p>
  </main>
</body>
</html>
```